Banner 170x60 for Barrel Sauna Rental Banner

Attention, please do every side graphic distance 5cm . It is for attachment.
search for a graphic design in dimension 170x60cm.
we have a barrel sauna rental service and need a banner for the two sides.
please look photos.
big text is: (SAUNA ZU MIETEN )in english like: you can rent me
frohe-kistenwelt.de
015293417720
info@frohe-kistenwelt.de
we need an eye catcher design!!!!
Design:
maybe wood in at background.
maybe burning fire and sauna style.
Please don't use my barrell sauna pictures. It is only an example for you what we do. The barrel sauna is on build at the moment.

```html
<!DOCTYPE html>
<html lang="de">
<head>
<meta charset="utf-8">
<title>Banner – Sauna zu mieten</title>
<link rel="stylesheet" href="https://fonts.googleapis.com/css2?family=Roboto+Condensed:wght@700&display=swap">
<style>
  :root {
    --stage-dark: #1c1b1b;
    --stage-light: #ffffff;
    --wood-deep: #2a140a;
    --wood-mid: #6e3818;
    --wood-warm: #a05a28;
    --text-white: #ffffff;
    --accent-yellow: #ffe800;
    --divider: #1a0d06;
    --frame-gray: #8a8a8a;
  }
  * { margin: 0; padding: 0; box-sizing: border-box; }
  html, body {
    width: 1200px;
    height: 1200px;
    overflow: hidden;
  }
  body {
    position: relative;
    font-family: "Roboto Condensed", "Arial Narrow", sans-serif;
    font-weight: 700;
    background: var(--stage-light);
  }
  .stage-dark {
    position: absolute;
    left: 0; top: 0;
    width: 1200px;
    height: 557px;
    background: var(--stage-dark);
  }
  .banner {
    position: absolute;
    left: 384px;
    width: 410px;
    height: 146px;
    overflow: hidden;
  }
  .banner--on-dark { top: 197px; outline: 2px solid var(--frame-gray); }
  .banner--on-light { top: 782px; }
  .banner__wood {
    position: absolute;
    inset: 0;
    background:
      linear-gradient(90deg, rgba(20,8,3,0.7) 0%, rgba(20,8,3,0) 25%, rgba(20,8,3,0) 55%, rgba(20,8,3,0.85) 100%),
      linear-gradient(180deg, var(--wood-mid) 0%, var(--wood-warm) 30%, var(--wood-mid) 55%, var(--wood-warm) 75%, var(--wood-deep) 100%);
  }
  .banner__headline {
    position: absolute;
    left: 14px;
    top: 14px;
    width: 122px;
    color: var(--text-white);
    font-size: 38px;
    line-height: 37px;
    letter-spacing: 0;
    text-transform: uppercase;
  }
  .banner__divider {
    position: absolute;
    left: 142px;
    top: 12px;
    width: 4px;
    height: 122px;
    background: var(--divider);
  }
  .banner__contact {
    position: absolute;
    left: 161px;
    top: 16px;
    color: var(--text-white);
  }
  .contact__web { display: block; font-size: 26px; line-height: 30px; letter-spacing: -0.3px; }
  .contact__phone { display: block; font-size: 37px; line-height: 46px; color: var(--accent-yellow); letter-spacing: -0.5px; }
  .contact__mail { display: block; font-size: 22px; line-height: 28px; letter-spacing: -0.4px; }
</style>
</head>
<body>
  <div class="stage-dark"></div>

  <section class="banner banner--on-dark">
    <div class="banner__wood" role="img" aria-label="Warm wooden plank background with darkened edges"></div>
    <h1 class="banner__headline">Sauna<br>zu<br>mieten</h1>
    <div class="banner__divider"></div>
    <div class="banner__contact">
      <span class="contact__web">frohe-kistenwelt.de</span>
      <span class="contact__phone">015293417720</span>
      <span class="contact__mail">info@frohe-kistenwelt.de</span>
    </div>
  </section>

  <section class="banner banner--on-light">
    <div class="banner__wood" role="img" aria-label="Warm wooden plank background with darkened edges"></div>
    <h2 class="banner__headline">Sauna<br>zu<br>mieten</h2>
    <div class="banner__divider"></div>
    <div class="banner__contact">
      <span class="contact__web">frohe-kistenwelt.de</span>
      <span class="contact__phone">015293417720</span>
      <span class="contact__mail">info@frohe-kistenwelt.de</span>
    </div>
  </section>
</body>
</html>
```